Business Card Design with new logo

Dorian Pelleway 4172
E 118th St Harrowmere, ZZ 00000
Cell: 217-555-0193
pellewayrestoration@mailvane.test

Classic Car Restoration Services Buy Sell Trade Consign

Dorian Pelleway 9698
Cell: 217-555-0193

```html
<!DOCTYPE html>
<html lang="en">
<head>
<meta charset="utf-8">
<title>Pelleway Restoration LLC – Business Card</title>
<link rel="stylesheet" href="https://fonts.googleapis.com/css2?family=Open+Sans:ital,wght@0,600;0,700;1,700&display=swap">
<style>
  :root {
    --backdrop: #3b3b3b;
    --card-light: #ffffff;
    --card-dark: #333333;
    --brand-red: #c43439;
    --ink-light: #ffffff;
  }
  * { margin: 0; padding: 0; box-sizing: border-box; }
  html, body {
    width: 1200px; height: 801px; overflow: hidden;
    background: var(--backdrop);
    font-family: "Open Sans", Arial, sans-serif;
  }
  .stage { position: relative; width: 1200px; height: 801px; }
  .card {
    position: absolute; top: 260px; width: 495px; height: 282px;
    border-radius: 12px; overflow: hidden;
  }
  .card--front { left: 89px; background: var(--card-light); }
  .card--back { left: 620px; background: var(--card-dark); }
  .wordmark {
    position: absolute; left: 0; right: 0;
    display: flex; align-items: center; justify-content: center; gap: 12px;
  }
  .card--front .wordmark { top: 118px; }
  .card--back .wordmark { top: 92px; }
  .wordmark__dot {
    width: 26px; height: 26px; border-radius: 50%;
    background: var(--brand-red); flex: none;
  }
  .wordmark__name {
    font-weight: 700; font-size: 22px; letter-spacing: 1px;
    text-transform: uppercase; color: var(--brand-red);
  }
  .contact {
    position: absolute; left: 0; right: 0; top: 183px;
    color: var(--ink-light); font-size: 12px; font-weight: 600;
    display: flex; flex-direction: column; align-items: center; gap: 6px;
  }
  .contact__row { display: flex; align-items: center; gap: 8px; }
  .contact__item { display: flex; align-items: center; gap: 4px; white-space: nowrap; }
  .contact__icon { width: 11px; height: 11px; flex: none; }
  .tagline-band {
    position: absolute; left: 0; right: 0; top: 236px; height: 26px;
    background: var(--brand-red);
    display: flex; align-items: center; justify-content: center;
  }
  .tagline {
    color: var(--ink-light); font-size: 13.5px; font-weight: 700; font-style: italic;
  }
</style>
</head>
<body>
<main class="stage">
  <section class="card card--front">
    <div class="wordmark">
      <span class="wordmark__dot"></span>
      <span class="wordmark__name">Pelleway Restoration LLC</span>
    </div>
    <div class="tagline-band"><p class="tagline">Classic Car Restoration Services Buy Sell Trade Consign</p></div>
  </section>

  <section class="card card--back">
    <div class="wordmark">
      <span class="wordmark__dot"></span>
      <span class="wordmark__name">Pelleway Restoration LLC</span>
    </div>
    <div class="contact">
      <div class="contact__row">
        <span class="contact__item">
          <svg class="contact__icon" viewBox="0 0 12 12"><circle cx="6" cy="6" r="6" fill="#c43439"/><path d="M6 2.5a2 2 0 0 0-2 2c0 1.6 2 4.5 2 4.5s2-2.9 2-4.5a2 2 0 0 0-2-2z" fill="#fff"/></svg>
          Dorian Pelleway 4172
        </span>
        <span class="contact__item">
          <svg class="contact__icon" viewBox="0 0 12 12"><circle cx="6" cy="6" r="6" fill="#c43439"/><path d="M3 6.5l6-3-2 6-1-2.5z" fill="#fff"/></svg>
          E 118th St Harrowmere, ZZ 00000
        </span>
      </div>
      <div class="contact__row">
        <span class="contact__item">
          <svg class="contact__icon" viewBox="0 0 12 12"><circle cx="6" cy="6" r="6" fill="#c43439"/><path d="M4 3l1.2 1.6-.6.8a4 4 0 0 0 2 2l.8-.6L9 8l-.8 1A5 5 0 0 1 3 3.8z" fill="#fff"/></svg>
          217-555-0193
        </span>
        <span class="contact__item">
          <svg class="contact__icon" viewBox="0 0 12 12"><circle cx="6" cy="6" r="6" fill="#c43439"/><circle cx="6" cy="6" r="3.2" fill="none" stroke="#fff" stroke-width="0.9"/><path d="M2.8 6h6.4M6 2.8v6.4" stroke="#fff" stroke-width="0.8"/></svg>
          pellewayrestoration@mailvane.test
        </span>
      </div>
    </div>
    <div class="tagline-band"><p class="tagline">Classic Car Restoration Services Buy Sell Trade Consign</p></div>
  </section>
</main>
</body>
</html>
```